The Garden Gate Circle website look (Wordpress)

We need a new website ~ wordpress design preferrably ~ to capture our personality .. unique and feminine, without being too girly or prissy! We are a business women's networking group which has been described as vibrant, rowdy and fun; a safe place for women to gather; holistic; and a little bit edgy. Unique and down to earth. Originally created by two close friends who met when their kids were in kindergarten together and out of a shared passion to encourage women to be more than a spectator to life; to create flexible, viable sources of income in order to allow more time for family, friends and other passions.
Our current website is: www.tggc.com.au
We have had a local designer working on our new website but are not satisfied:
http://www.craftventurepages.com/dev-sites/tggc/
Facebook page is: www.facebook.com/TGGC1
We are expanding and have branches in Cleveland, Coffs Harbour, Gold Coast and Springwood.
Inspiration sites: www.meadowlarkhaven.com (although background needs to be lighter!)
http://www.thebrightpathcollective.com (great content for a networking site but we need a little brighter).

Target Market(s)

Women aged between 30-50 juggling career and family. Fun, real, creative, vibrant, energetic, alive.

Industry/Entity Type

Business

Requirements
Must have
• Our colour scheme is pink and aqua (some bold; some pale .. see uploaded files for logo).
Two of our most often used taglines ~ and at least one of these should appear somewhere prominently so that page visitors can know right away what we do:
1. "A place for women to connect ~ business growth and personal development in a positive environment"
2. "The monthly event women DO look forward to.."
A feature of our website needs to be 'people' .. happy smiling faces and movement in a slider section (have uploaded some pics for inclusion but would like provision to add more).
Website must have provision for several tabs as there are many facets to our networking group. Must have a 'subscribe now for our top 10 networking tips' button (something a little funky :-) Must also have room somewhere for up to five major sponsor logos/advertising and a bold link to our forum.
One of the features of our group is the use of inspirational quotes .. we'll need to have a place on front page where quotes are displayed/alternated .. if you want an example, use "Well behaved women rarely make history" ~ Marion Delacourt Hayes
This is the first project I've listed so not sure how much detail to include re names of tabs etc.
Facebook and Pinterest tabs.
Nice to have
• Preferrably a white background but would like an impression or watermark image (possibly in very pale grey, pink or aqua) of a floral or scroll .. something that will tie in with the rest of the page.

Happy for you to surprise us with a design a little bit out of the square :-)
Should not have
• Should not be too 'kitchy' or too girly (the pics we've included have enough 'feminine' to carry that through, I think). The name of our company 'The Garden Gate Circle' refers to the concept of a Kitchen Table Entrepreneur and is aimed at a not-so-conservative, less formal, more open, honest and real woman, most likely a mother who is juggling both family and career.

```html
<!DOCTYPE html>
<html lang="en">
<head>
<meta charset="utf-8">
<title>The Garden Gate Circle</title>
<link href="https://fonts.googleapis.com/css2?family=Lato:ital,wght@0,400;0,700;1,400&family=Crimson+Text:wght@400;600&display=swap" rel="stylesheet">
<style>
:root{
  --teal:#0b8fb0;
  --teal-dark:#0a7c99;
  --aqua-top:#0a9cc0;
  --aqua-pale:#dff5fc;
  --aqua-band:#bfeaf6;
  --aqua-foot:#a9e0f0;
  --pink:#e0457f;
  --pink-pale:#f9d6e3;
  --pink-badge:#ee9dbb;
  --grey:#7b7b7b;
  --white:#ffffff;
}
*{box-sizing:border-box;margin:0;padding:0}
html,body{width:753px;height:1200px;overflow:hidden}
body{font-family:"Lato",Arial,sans-serif;color:var(--teal);position:relative;
  background:linear-gradient(180deg,var(--aqua-pale) 0,#eefafe 380px,var(--white) 520px,var(--white) 100%)}
a{text-decoration:none}
.abs{position:absolute}
.top-bar{left:0;top:0;width:753px;height:10px;background:var(--aqua-top)}
.brand{left:24px;top:22px;display:flex;align-items:center;gap:12px}
.brand-mark{width:46px;height:84px;background:linear-gradient(135deg,var(--pink) 0,var(--pink) 50%,#39b4d3 50%,#39b4d3 100%)}
.brand-name{font-size:15px;line-height:18px;color:var(--teal);width:130px}
.nav{left:265px;top:14px;height:100px}
.nav-item{position:absolute;top:0;height:96px;text-align:center;font-size:11px;color:var(--teal)}
.nav-item svg{position:absolute;left:50%;top:36px;transform:translateX(-50%)}
.nav-item span{position:absolute;left:0;right:0;top:70px}
.nav-sep{position:absolute;top:0;height:94px;border-left:1px dashed #6cc3da}
.nav-main{position:absolute;left:0;top:31px;width:64px;height:64px;border-radius:50%;background:var(--white);border:2px solid #bfe6f1;text-align:center;font-size:11px}
.nav-main svg{margin-top:8px}
.nav-main span{display:block;margin-top:4px}
.hero{left:18px;top:124px;width:712px;height:235px;background:#c9eef8;padding:4px}
.hero-photo{width:704px;height:227px;background:linear-gradient(90deg,#d8cbb6 0%,#efe6da 22%,#e2c8a6 33%,#5b3f5e 45%,#e9ddd0 56%,#caa49a 64%,#f0b9c7 75%,#e6d9cd 88%,#cfb7a8 100%)}
.hero-tag{left:22px;top:222px;width:282px;height:66px;background:var(--white);clip-path:polygon(0 0,100% 0,88% 100%,0 100%);
  font-family:"Crimson Text",Georgia,serif;font-size:18px;line-height:24px;color:var(--pink);padding:7px 0 0 18px}
.section-title{font-family:"Crimson Text",Georgia,serif;font-weight:400;font-size:15.5px;color:var(--teal)}
.welcome{left:22px;top:378px;width:492px}
.welcome .section-title{border-bottom:1px dotted #9fd9e8;padding-bottom:6px;width:240px;margin-bottom:9px}
.welcome p{font-size:8px;line-height:11.7px;margin-bottom:4px}
.col-divider{left:523px;top:382px;height:592px;border-left:1px solid #f3c6d6}
.card{position:absolute;width:242px}
.card-photo{height:98px;background:#d6eef5;padding:4px}
.card-photo div{height:92px;clip-path:polygon(0 0,100% 0,100% 84%,96% 100%,92% 84%,88% 100%,84% 84%,80% 100%,76% 84%,72% 100%,68% 84%,64% 100%,60% 84%,56% 100%,52% 84%,48% 100%,44% 84%,40% 100%,36% 84%,32% 100%,28% 84%,24% 100%,20% 84%,16% 100%,12% 84%,8% 100%,4% 84%,0 100%)}
.card h3{font-size:9px;font-weight:400;margin:12px 0 3px 5px}
.card p{font-size:8px;line-height:11.8px;margin-left:5px;width:228px}
.read-more{display:block;margin:10px 0 0 4px;width:228px;height:16px;background:var(--pink-pale);font-size:8px;line-height:16px;padding-left:8px;color:var(--teal-dark)}
.blog{left:540px;top:388px;width:180px}
.blog .section-title{border-bottom:1px dotted #9fd9e8;padding-bottom:6px;margin-bottom:12px}
.post{margin-bottom:14px;margin-left:3px}
.post-date{font-size:12.5px;color:var(--pink);margin-bottom:4px}
.post p{font-size:8px;line-height:12.8px;font-style:italic;color:var(--grey)}
.post-more{display:block;margin-top:8px;width:158px;height:15px;background:var(--pink-pale);border-radius:3px;font-size:7px;line-height:15px;padding-left:6px;color:#8a6070;position:relative}
.post-more::after{content:"›";position:absolute;right:8px;color:var(--white);font-size:11px}
.subscribe{left:550px;top:787px}
.footer{left:0;top:990px;width:753px;height:166px;background:var(--aqua-band);border-top:3px solid #d3f0f8}
.footer-dash{left:0;top:997px;width:753px;border-top:1px dashed #5cbad4}
.footer h4{position:absolute;font-weight:400;font-size:11.5px;color:var(--teal)}
.foot-link{position:absolute;font-size:8px;color:var(--teal-dark);padding-left:14px}
.foot-link::before{content:"";position:absolute;left:0;top:2px;width:8px;height:5px;border-radius:50%;background:var(--teal)}
.partner-a{left:392px;top:1045px;width:64px;height:82px;background:linear-gradient(180deg,#f7f7f7 0,#eef3f7 40%,#6aa7d0 70%,#1f5f94 100%)}
.partner-b{left:478px;top:1050px;width:160px;height:26px;background:linear-gradient(90deg,#8ccc55,#5db8d6)}
.copy-bar{left:0;top:1156px;width:753px;height:34px;background:var(--aqua-foot);font-size:8px;color:var(--teal-dark);padding:12px 0 0 20px}
</style>
</head>
<body>
<div class="abs top-bar"></div>

<header class="abs brand">
  <div class="brand-mark"></div>
  <div class="brand-name">The Garden Gate Circle</div>
</header>

<nav class="abs nav">
  <div class="nav-main">
    <svg width="22" height="20" viewBox="0 0 22 20"><path d="M2 10 11 2l9 8" fill="none" stroke="#2a8fd0" stroke-width="2.4"/><rect x="5" y="10" width="12" height="9" fill="#2a8fd0"/></svg>
    <span>Main</span>
  </div>
  <div class="nav-sep" style="left:72px"></div>
  <div class="nav-item" style="left:76px;width:42px">
    <svg width="22" height="20" viewBox="0 0 22 20"><rect x="1" y="2" width="20" height="17" fill="#e8f2f7" stroke="#3a8fc0"/><rect x="1" y="2" width="20" height="4" fill="#3a8fc0"/></svg><span>Events</span></div>
  <div class="nav-sep" style="left:123px"></div>
  <div class="nav-item" style="left:132px;width:62px">
    <svg width="26" height="22" viewBox="0 0 26 22"><circle cx="10" cy="6" r="5" fill="#2a8fd0"/><path d="M1 21c1-7 17-7 18 0z" fill="#2a8fd0"/><rect x="16" y="8" width="9" height="8" fill="#6bb5e3"/></svg><span>Membership</span></div>
  <div class="nav-sep" style="left:205px"></div>
  <div class="nav-item" style="left:210px;width:56px">
    <svg width="26" height="20" viewBox="0 0 26 20"><path d="M1 3h9l2 3h13v13H1z" fill="#2fa6df"/></svg><span>Directory</span></div>
  <div class="nav-sep" style="left:271px"></div>
  <div class="nav-item" style="left:279px;width:66px">
    <svg width="26" height="22" viewBox="0 0 26 22"><path d="M2 12l7-8 6 3 7-3 2 8-9 8z" fill="none" stroke="#1f8ccc" stroke-width="2"/></svg><span>Sponsorship</span></div>
  <div class="nav-sep" style="left:352px"></div>
  <div class="nav-item" style="left:358px;width:34px">
    <svg width="22" height="22" viewBox="0 0 22 22"><ellipse cx="11" cy="9" rx="10" ry="8" fill="#3aa7e0"/><path d="M6 15l-2 6 7-5z" fill="#3aa7e0"/></svg><span>Blog</span></div>
  <div class="nav-sep" style="left:398px"></div>
  <div class="nav-item" style="left:405px;width:46px">
    <svg width="24" height="20" viewBox="0 0 24 20"><path d="M2 6c0-4 20-4 20 0v3h-5V6H7v3H2z" fill="#3a8fc0"/><rect x="5" y="9" width="14" height="10" rx="2" fill="#5aa9d6"/></svg><span>Contact</span></div>
</nav>

<section class="abs hero">
  <div class="hero-photo" role="img" aria-label="Two smiling women seated together at a kitchen table, one in purple and one in pink"></div>
</section>
<div class="abs hero-tag">A place for women to connect<br>in a positive environment"</div>

<section class="abs welcome">
  <h2 class="section-title">Welcome to Our Website Mainpage</h2>
  <p>Brightloom Webworks is a web service company, offering a wide range of services which range from designing and development, that is covering almost all the fields in the best possible way. To be the best we know what and how to present beautifully the working of the client's need and their advantages be highlighted. We act in accordance with the Industry certified processes to deliver the best to our clients all over the world. Over years we have built a strong reputation in providing website design and web development services.</p>
  <p>Thus, Wanna get ahead in the competition with other websites.... Brightloom Webworks provide you with an attractive and most convincing website to enhance your marketing goals.</p>
  <p>The only way to success is through the right path and that's what we provide you. None of the other companies has the result we do. So stick to the best that's how you will be the best don't opt for the second best.</p>
</section>

<div class="abs col-divider"></div>

<article class="card" style="left:16px;top:551px">
  <div class="card-photo"><div role="img" aria-label="Two women smiling side by side in front of a brick wall" style="background:linear-gradient(90deg,#c9c9cc 0%,#8d8f98 18%,#1f2d5a 35%,#e8d8cc 52%,#f0c9a0 68%,#d0a47e 80%,#c63a3c 100%)"></div></div>
  <h3>YOUR SERVICES HERE !</h3>
  <p>Brightloom Webworks is a web service company, offering a wide range of services which range from designing and development, that is covering almost all the fields in the best possible way.</p>
  <a class="read-more">READ MORE</a>
</article>
<article class="card" style="left:262px;top:551px">
  <div class="card-photo"><div role="img" aria-label="Two laughing women close together" style="background:linear-gradient(90deg,#6b4a33 0%,#c99770 20%,#eac6a6 40%,#8a6446 55%,#e3bb95 72%,#c4946d 88%,#5c3f2c 100%)"></div></div>
  <h3>YOUR SERVICES HERE !</h3>
  <p>Brightloom Webworks is a web service company, offering a wide range of services which range from designing and development, that is covering almost all the fields in the best possible way.</p>
  <a class="read-more">READ MORE</a>
</article>
<article class="card" style="left:16px;top:764px">
  <div class="card-photo"><div role="img" aria-label="Women in race day hats laughing together" style="background:linear-gradient(90deg,#2b2426 0%,#d8a792 18%,#d94050 32%,#f1e4dc 45%,#3a3031 58%,#e6c2ad 72%,#1f1b1d 86%,#b8cf8a 100%)"></div></div>
  <h3>YOUR SERVICES HERE !</h3>
  <p>Brightloom Webworks is a web service company, offering a wide range of services which range from designing and development, that is covering almost all the fields in the best possible way.</p>
  <a class="read-more">READ MORE</a>
</article>
<article class="card" style="left:266px;top:764px">
  <div class="card-photo"><div role="img" aria-label="Group of women in caps at a golf day" style="background:linear-gradient(90deg,#7e9a6a 0%,#f4f4f2 16%,#ededeb 30%,#2a2a30 44%,#e85a9a 58%,#f2f2f0 72%,#d04a72 84%,#5f7d4e 100%)"></div></div>
  <h3>YOUR SERVICES HERE !</h3>
  <p>Brightloom Webworks is a web service company, offering a wide range of services which range from designing and development, that is covering almost all the fields in the best possible way.</p>
  <a class="read-more">READ MORE</a>
</article>

<aside class="abs blog">
  <h2 class="section-title">Recent Blog &amp; News</h2>
  <div class="post">
    <div class="post-date">20.05.2012</div>
    <p>E-Commerce is a major progress in technology that has changed the way in which the customers now purchase information, products and the services. It's the new way of providing an opportunity to make your products and services available in the global market 24 hours a day through Internet</p>
    <a class="post-more">CLICK HERE TO READ MORE</a>
  </div>
  <div class="post">
    <div class="post-date">20.05.2012</div>
    <p>E-Commerce is a major progress in technology that has changed the way in which the customers now purchase information, products and the services.</p>
    <a class="post-more">CLICK HERE TO READ MORE</a>
  </div>
  <div class="post">
    <div class="post-date">20.05.2012</div>
    <p>E-Commerce is a major progress in technology that has changed the way in which the customers now purchase information, products and the services.</p>
    <a class="post-more">CLICK HERE TO READ MORE</a>
  </div>
</aside>

<svg class="abs subscribe" width="158" height="158" viewBox="0 0 158 158" role="img" aria-label="Subscribe for our top ten networking tips">
  <circle cx="79" cy="79" r="78" fill="var(--pink-badge)"/>
  <circle cx="79" cy="79" r="72" fill="none" stroke="#fff" stroke-width="1.5" stroke-dasharray="3 3"/>
  <circle cx="79" cy="79" r="66" fill="#fde9f0"/>
  <circle cx="79" cy="79" r="52" fill="#e4e4e4" stroke="#7a7a7a" stroke-width="1.5"/>
  <rect x="14" y="64" width="130" height="30" fill="#fde9f0" stroke="#8a8a8a" stroke-width="1"/>
  <text x="79" y="88" text-anchor="middle" font-family="Crimson Text, Georgia, serif" font-size="25" fill="#555" letter-spacing="1">SUBSCRIBE</text>
</svg>

<footer class="abs footer">
  <h4 style="left:30px;top:25px">More Information</h4>
  <a class="foot-link" style="left:30px;top:58px">Main page</a>
  <a class="foot-link" style="left:30px;top:79px">About Our Company</a>
  <a class="foot-link" style="left:30px;top:100px">Services</a>
  <a class="foot-link" style="left:30px;top:121px">Blog</a>
  <a class="foot-link" style="left:145px;top:58px">Support &amp; FAQ</a>
  <a class="foot-link" style="left:145px;top:79px">Recent News</a>
  <a class="foot-link" style="left:145px;top:100px">Our Services</a>
  <a class="foot-link" style="left:145px;top:121px">Testimonials</a>
  <a class="foot-link" style="left:265px;top:58px">Recent Projects</a>
  <a class="foot-link" style="left:265px;top:79px">Communicate</a>
  <a class="foot-link" style="left:265px;top:100px">Social Networking</a>
  <a class="foot-link" style="left:265px;top:121px">Contact</a>
  <h4 style="left:392px;top:25px">Our Partners</h4>
</footer>
<div class="abs footer-dash"></div>
<div class="abs partner-a" role="img" aria-label="Partner badge"></div>
<div class="abs partner-b" role="img" aria-label="Partner badge"></div>
<div class="abs copy-bar">copyright © 2012 Company Name &nbsp;|&nbsp; All right reserved</div>
</body>
</html>
```